Tarvell Consulting needs a Business Catalogue

We are looking at creating a business catalogue that is used to introduce ourselves and our business as well as the services we offer. We are an HR business that offers assistance with recruitment and selection and all services involved in that area. We don't offer specific products and don't have prices advertised. it would be good to start with an introduction to the business and our history, some staff bios then a framework to discuss business scenarios where we can help. I would prefer white as the main colour on the front/back page with the colours of the logo (attached) to be used throughout the catalogue along with images and other visual improvements. A mall amount of colour should be used throughout and don't want solid colour pages. Prefer what pages that are broken up by coloured designs, images, diagrams heading etc. A 12-page catalogue with different designs I can move around as needed would be good.

Target Market(s)

Education, government, large business with administration staff

Font styles to use
Sans Serif

Requirements
Must have
• Logo colour scheme
• Images, diagrams, tables etc
• Start with company introduction (history, three staff profiles, company values etc)
• Main section will be the description of services and processes offered.
Nice to have
• A range of different visuals to choose from including designs for tables, paragraphs, diagrams, space for photos and other visual elements.

```html
<!DOCTYPE html>
<html lang="en">
<head>
<meta charset="utf-8">
<title>Tarvell Consulting – Assistance with Recruitment and Selection</title>
<link rel="stylesheet" href="https://fonts.googleapis.com/css2?family=Oswald:wght@300;400&display=swap">
<style>
  :root {
    --paper: #ffffff;
    --ink: #1f1f22;
    --ink-soft: #3c3f44;
    --photo-light: #f5f8fb;
    --photo-mist: #e4ebf2;
    --photo-mid: #c8d5e2;
    --photo-cool: #b9cadb;
    --accent: #2f7fc1;
  }
  * { margin: 0; padding: 0; box-sizing: border-box; }
  html, body {
    width: 848px;
    height: 1200px;
    overflow: hidden;
    background: var(--paper);
  }
  .cover {
    position: relative;
    width: 848px;
    height: 1200px;
    background: var(--paper);
    font-family: "Oswald", "Arial Narrow", sans-serif;
    overflow: hidden;
  }
  .cover-photo {
    position: absolute;
    inset: 0 0 auto 0;
    height: 1045px;
    background:
      linear-gradient(90deg, rgba(210,220,230,0.55) 0%, rgba(255,255,255,0) 30%, rgba(255,255,255,0) 70%, rgba(200,212,225,0.45) 100%),
      linear-gradient(180deg, var(--photo-light) 0%, var(--photo-mist) 40%, var(--photo-mid) 72%, var(--photo-cool) 82%, #e6edf4 100%);
  }
  .white-cut {
    position: absolute;
    left: 0;
    top: 0;
    width: 848px;
    height: 1200px;
  }
  .cover-title {
    position: absolute;
    right: 63px;
    top: 680px;
    text-align: right;
    color: var(--ink);
    font-weight: 300;
    font-size: 51px;
    line-height: 71px;
    letter-spacing: 0.5px;
    text-transform: uppercase;
  }
  .brand {
    position: absolute;
    right: 62px;
    top: 1068px;
    display: flex;
    align-items: center;
    gap: 16px;
  }
  .brand-mark {
    width: 22px;
    height: 22px;
    background: var(--accent);
  }
  .brand-name {
    font-weight: 300;
    font-size: 30px;
    letter-spacing: 3px;
    color: var(--ink-soft);
    text-transform: uppercase;
  }
</style>
</head>
<body>
  <main class="cover">
    <div class="cover-photo" role="img" aria-label="Photo placeholder: softly blurred business meeting in a bright office"></div>
    <svg class="white-cut" viewBox="0 0 848 1200" aria-hidden="true">
      <polygon points="0,1045 428,1045 463,983 848,983 848,1200 0,1200" fill="var(--paper)"/>
    </svg>
    <h1 class="cover-title">Assistance<br>with recruitment<br>and selection</h1>
    <div class="brand">
      <span class="brand-mark"></span>
      <span class="brand-name">Tarvell Consulting</span>
    </div>
  </main>
</body>
</html>
```